Book Cover Design for Educational Assessment Book

We are a publisher based in Singapore. We need a book cover design for an educational assessment book titled "Keystone Tier Advanced Numeracy Drill Compendium". The book is targeted at high school students, hence the design should look professional and not overly fanciful. This book is the first in a series. Subsequent books will have the same design but of different theme colours. Designers need to take note that the design must allow for different theme colours to be used. Please refer to the attached file 'Syllabus' for the mathematical concepts taught in our book.

Target Market(s)

Singapore Keystone Tier Students/ High School Students

Industry/Entity Type

Education

Requirements
Must have
• 1. A Space for Company Logo on top right
• 2. A Space for ISBN number on bottom right (to be provided later)
• 3. Book Highlights:
• a. "The Most Comprehensive Advanced Numeracy Drill Compendium"
• b. "More than 1000 Questions"
• c. "With Step-by-Step Complete Solutions"
• d. "Latest NCA Syllabus - Syllabus 7132"
• e. "Questions Booklet"
Nice to have
• Nice to have a theme colour, so we can allocate different colours to subsquent books in the same series.
• Nice to have appropriate and simple mathematical graphics or formulae.
Should not have
• Cartoons, Photographs, Flamboyant Graphics

```html
<!DOCTYPE html>
<html lang="en">
<head>
<meta charset="utf-8">
<title>Keystone Tier Advanced Numeracy Drill Compendium — Cover</title>
<link rel="stylesheet" href="https://fonts.googleapis.com/css2?family=Oswald:wght@400;600;700&family=Caveat:wght@500;700&family=Open+Sans:wght@400;600&display=swap">
<style>
  :root {
    --theme: #f7c51e;
    --ink: #1a1a1a;
    --board: #262626;
    --board-edge: #111111;
    --chalk: #f3f1ea;
    --chalk-theme: #f2c62a;
    --accent-green: #5f8f3a;
    --accent-orange: #e08a1e;
    --stage: #e9e6e1;
    --paper: #ffffff;
    --muted: #8a8a8a;
  }
  * { box-sizing: border-box; margin: 0; padding: 0; }
  html, body { width: 1200px; height: 933px; overflow: hidden; }
  body { background: var(--stage); position: relative; font-family: "Open Sans", sans-serif; }

  .cover {
    position: absolute; left: 300px; top: 66px;
    width: 600px; height: 800px;
    background: var(--theme);
    box-shadow: 0 10px 30px rgba(0,0,0,.18);
    overflow: hidden;
  }
  .cover__header { position: absolute; left: 0; top: 0; width: 600px; height: 410px; background: var(--theme); }

  .publisher-mark {
    position: absolute; right: 34px; top: 28px;
    width: 74px; height: 74px; background: var(--paper);
    display: flex; align-items: center; justify-content: center;
    font-family: "Open Sans", sans-serif; font-weight: 600; font-size: 11px; color: var(--ink);
    text-align: center; line-height: 1.2;
  }

  .title-block { position: absolute; left: 60px; top: 110px; color: var(--ink); }
  .title-block__tier { font-family: "Oswald", sans-serif; font-weight: 600; font-size: 20px; line-height: 1.1; }
  .title-block__main { font-family: "Oswald", sans-serif; font-weight: 700; font-size: 44px; line-height: 1.02; letter-spacing: -.3px; }
  .title-block__sub { font-family: "Oswald", sans-serif; font-weight: 400; font-size: 20px; letter-spacing: 1px; text-transform: uppercase; line-height: 1.15; }

  .highlight { position: absolute; color: var(--ink); }
  .highlight__script { font-family: "Caveat", cursive; font-weight: 700; line-height: 1; white-space: nowrap; }
  .highlight__note { font-family: "Open Sans", sans-serif; font-size: 9.5px; line-height: 1.3; white-space: nowrap; }

  .hl-most { left: 240px; top: 232px; }
  .hl-most .highlight__script { font-size: 46px; }
  .hl-most .highlight__note { margin-left: 20px; }

  .hl-steps { left: 60px; top: 312px; }
  .hl-steps .highlight__script { font-size: 30px; }

  .hl-count { left: 360px; top: 306px; }
  .hl-count .highlight__script { font-size: 30px; color: var(--accent-green); }

  .hl-latest { left: 250px; top: 356px; }
  .hl-latest .highlight__script { font-size: 26px; color: var(--accent-orange); }

  .hl-booklet { left: 430px; top: 354px; }
  .hl-booklet .highlight__script { font-size: 30px; color: var(--accent-orange); }

  .cover__board {
    position: absolute; left: 0; top: 410px; width: 600px; height: 390px;
    background: radial-gradient(ellipse at 40% 40%, #333333 0%, var(--board) 55%, var(--board-edge) 100%);
  }
  .board-art {
    position: absolute; left: 50px; top: 30px; width: 230px; height: 300px;
    border-radius: 12px;
    background: linear-gradient(160deg, #4a4120 0%, #3a3420 50%, #2e2b22 100%);
  }
  .formulas {
    position: absolute; left: 310px; top: 60px; list-style: none;
    font-family: "Caveat", cursive; font-weight: 500; font-size: 26px; color: var(--chalk); line-height: 1.7;
  }
  .isbn-space {
    position: absolute; right: 30px; bottom: 26px;
    width: 150px; height: 80px; background: var(--paper);
    display: flex; align-items: flex-end; justify-content: center; padding-bottom: 8px;
    font-family: "Open Sans", sans-serif; font-size: 10px; color: var(--muted); letter-spacing: .5px;
  }
</style>
</head>
<body>
  <main class="cover">
    <section class="cover__header">
      <div class="publisher-mark">Lumen<br>Press</div>

      <div class="title-block">
        <p class="title-block__tier">Keystone Tier</p>
        <h1 class="title-block__main">Advanced Numeracy</h1>
        <p class="title-block__sub">Drill Compendium</p>
      </div>

      <div class="highlight hl-most">
        <p class="highlight__script">“the most</p>
        <p class="highlight__note">comprehensive advanced numeracy drill compendium”</p>
      </div>

      <div class="highlight hl-steps">
        <p class="highlight__script">“with step by step</p>
        <p class="highlight__note">complete solutions”</p>
      </div>

      <div class="highlight hl-count">
        <p class="highlight__script">“more than</p>
        <p class="highlight__note">1000 questions”</p>
      </div>

      <div class="highlight hl-latest">
        <p class="highlight__script">latest</p>
        <p class="highlight__note">NCA syllabus - syllabus 7132</p>
      </div>

      <div class="highlight hl-booklet">
        <p class="highlight__note">questions</p>
        <p class="highlight__script">booklet</p>
      </div>
    </section>

    <section class="cover__board">
      <div class="board-art" role="img" aria-label="Chalk drawing of a light bulb labelled good idea with a solution banner"></div>
      <ul class="formulas">
        <li>(ax − b)(cx − d)</li>
        <li>(ax − b)(cx − d)²</li>
        <li>(ax − b)(x² − 2)</li>
        <li>(x − a)² + (y − b)² = r²</li>
      </ul>
      <div class="isbn-space">ISBN</div>
    </section>
  </main>
</body>
</html>
```